Leadership Brenvale Brochure Design*

We host a local leadership development program every two years. We need a brochure to promote the program. We would like it to be 8 1/2 x 11, tri-fold. I have attached a Word document with the necessary info for the brochure. The brochure will be professionally printed. We would like the final design to be in InDesign.

Target Market(s)

Potential participants of our leadership program. They will be local leaders, male and female, from 30-60 years of age.

Requirements
Must have
• Content as detailed in the Word document attached. Our logo.
Nice to have
• A design that is attractive to young professionals.

```html
<!DOCTYPE html>
<html lang="en">
<head>
<meta charset="utf-8">
<title>Leadership Brenvale – Brochure Inside Spread</title>
<link rel="stylesheet" href="https://fonts.googleapis.com/css2?family=Noto+Serif:wght@400;700&family=Lato:wght@400;700&family=Open+Sans:wght@400;600&display=swap">
<style>
  :root{
    --bg:#e9e9e9;
    --paper:#ffffff;
    --orange:#e8832a;
    --blue:#34479a;
    --green:#3aa54a;
    --green-band:#3fae4c;
    --ink:#1f1f1f;
    --photo-a:#8a6a4c;
    --photo-b:#c9a27a;
  }
  *{box-sizing:border-box;margin:0;padding:0}
  html,body{width:1200px;height:800px;overflow:hidden;background:var(--bg)}
  .brochure{position:absolute;left:105px;top:17px;width:990px;height:765px;background:var(--paper);box-shadow:0 2px 10px rgba(0,0,0,.12);overflow:hidden}
  .panel{position:absolute;top:0;width:330px;height:765px}
  .panel--overview{left:0}
  .panel--schedule-a{left:330px}
  .panel--schedule-b{left:660px}
  .fold{position:absolute;top:0;width:1px;height:765px;background:rgba(0,0,0,.06)}
  .swoosh{position:absolute;left:0;top:0}
  .overview-title{position:absolute;left:28px;top:34px;font-family:"Noto Serif",serif;font-size:26px;color:var(--orange);font-weight:400}
  .overview-intro{position:absolute;left:28px;top:80px;width:282px;font-family:"Lato",sans-serif;font-size:13.5px;line-height:1.38;color:var(--ink)}
  .overview-goals{position:absolute;left:40px;top:290px;width:272px;list-style:none;font-family:"Lato",sans-serif;font-size:13.5px;line-height:1.38;color:var(--ink)}
  .overview-goals li{position:relative;padding-left:12px;margin-bottom:12px}
  .overview-goals li::before{content:"•";position:absolute;left:0}
  .photo-slot{position:absolute;left:0;top:510px;width:330px;height:255px;background:linear-gradient(160deg,var(--photo-b),var(--photo-a))}
  .schedule-title{position:absolute;left:352px;top:66px;font-family:"Noto Serif",serif;font-size:27px;font-weight:400;color:#fff}
  .session{position:absolute;width:300px;font-family:"Lato",sans-serif;color:var(--ink)}
  .session-title{font-family:"Open Sans",sans-serif;font-size:14.5px;font-weight:400;color:var(--green);text-transform:uppercase;line-height:1.35}
  .session-title .dot{margin:0 6px}
  .session-time{font-size:15px;margin:6px 0 9px}
  .session-topics{list-style:none;font-size:13.5px;line-height:1.42}
  .session-topics li{position:relative;padding-left:16px}
  .session-topics li::before{content:"•";position:absolute;left:0}
  .footer-band{position:absolute;left:330px;top:727px;width:660px;height:38px;background:var(--green-band);color:#fff;font-family:"Lato",sans-serif;font-size:10.5px;white-space:nowrap;display:flex;align-items:center;justify-content:center}
</style>
</head>
<body>
<main class="brochure">
  <svg class="swoosh" width="990" height="765" viewBox="0 0 990 765" aria-hidden="true">
    <path d="M330 0H990V130C900 100 780 70 660 60C520 90 400 150 330 210Z" fill="var(--orange)"/>
    <path d="M330 55C450 35 560 10 660 4C780 20 900 70 990 112V130C900 100 780 70 660 60C520 90 400 150 330 210Z" fill="var(--blue)"/>
    <path d="M0 455C80 495 200 510 330 495V510H0Z" fill="var(--orange)"/>
  </svg>

  <section class="panel panel--overview">
    <h2 class="overview-title">Project Overview</h2>
    <p class="overview-intro">Leadership Brenvale is a leadership certification program designed to prepare the leaders of tomorrow. During the five-month program, participants get an in-depth view of community issues, develop leadership skills necessary to assume leadership roles, and are exposed to community involvement opportunities. Leadership Brenvale will provide participants with the opportunities to:</p>
    <ul class="overview-goals">
      <li>Build and demonstrate leadership and communication skills</li>
      <li>Think critically about key business, policy, and civic issues facing Brenvale County</li>
      <li>Build meaningful, long-lasting connections</li>
      <li>Establish ongoing dialogues with experienced community leaders</li>
    </ul>
    <div class="photo-slot" role="img" aria-label="Group photo of program participants standing together indoors"></div>
  </section>

  <div class="fold" style="left:330px"></div>
  <div class="fold" style="left:660px"></div>

  <h2 class="schedule-title">Schedule</h2>

  <section class="panel panel--schedule-a">
    <article class="session" style="left:22px;top:208px">
      <h3 class="session-title">Jan 17<span class="dot">•</span>Organizational Retreat &amp; Dinner (Attendance Mandatory)</h3>
      <p class="session-time">10:00 A.M. – 7:00 P.M</p>
      <ul class="session-topics"><li>Introductions</li><li>Team Building</li><li>Motivation</li><li>Leadership Styles</li><li>Social Hour/Dinner</li></ul>
    </article>
    <article class="session" style="left:22px;top:392px">
      <h3 class="session-title">Jan 17<span class="dot">•</span>Business &amp; Industry</h3>
      <p class="session-time">8:30 A.M. – 4:00 P.M.</p>
      <ul class="session-topics"><li>Business &amp; Industry Panel</li><li>Tour of Keystone Fabrication facility</li><li>Tour of Harrow Tool Company</li><li>“Taking your vision into B&amp;I”</li></ul>
    </article>
    <article class="session" style="left:22px;top:550px">
      <h3 class="session-title">Feb 21<span class="dot">•</span>Education</h3>
      <p class="session-time">8:30 A.M. – 4:00 P.M.</p>
      <ul class="session-topics"><li>Tour of selected programs at RCC</li><li>College Career Program overview</li><li>Lunch at Brenvale Career and College Academy</li><li>Tour of BCCA</li><li>Overview of CTE program paths</li></ul>
    </article>
  </section>

  <section class="panel panel--schedule-b">
    <article class="session" style="left:22px;top:120px">
      <h3 class="session-title">Mar 14<span class="dot">•</span>Future Technologies &amp; Communications</h3>
      <p class="session-time">8:30 A.M. – 4:00 P.M</p>
      <ul class="session-topics"><li>RCC Presents interview</li><li>Trends and forecasts</li><li>Marketing &amp; communications panel</li></ul>
    </article>
    <article class="session" style="left:22px;top:264px">
      <h3 class="session-title">Apr 4<span class="dot">•</span>Government</h3>
      <p class="session-time">8:30 A.M. – 4:00 P.M</p>
      <ul class="session-topics"><li>Overview of state/federal government</li><li>Overview of city/county government</li><li>Tour of Pine Hollow Correctional Institute</li><li>Tour of courthouse</li><li>Judicial presentations</li></ul>
    </article>
    <article class="session" style="left:22px;top:426px">
      <h3 class="session-title">May 2<span class="dot">•</span>Health &amp; Wellness</h3>
      <p class="session-time">8:30 A.M. – 4:00 P.M</p>
      <ul class="session-topics"><li>Tour of Riverbend Hospice</li><li>Community Wellness Roundtable</li><li>Tour of Halloway Cancer Care Center</li><li>Virtual Medicine Tutorial</li><li>Tour of BRHS</li></ul>
    </article>
    <article class="session" style="left:22px;top:590px">
      <h3 class="session-title">Mar 1<span class="dot">•</span>Graduation Ceremony and Luncheon</h3>
      <p class="session-time">8:30 A.M. – 4:00 P.M</p>
      <ul class="session-topics"><li>Participants are encouraged to invite their employer/supervisor/mentor/special guest (x2)</li></ul>
    </article>
  </section>

  <footer class="footer-band">Brenvale Chamber of Commerce and Tourism • 214 N. Alder Street • Ashford, NC • 555.014.2290 • www.TheBrenvaleChamber.com</footer>
</main>
</body>
</html>
```